Real Estate "For Sale" Sign for construction company

We need a sign that we can use to hang on a post and place on the road when we sell a property. The sign will be simple and will need to mainly feature our logo (files attached), as well as the words "For Sale", and then our phone number "(555) 617 3489". The sign will hang on a post that'll look something like the attached picture.

Target Market(s)

Home buyers

Industry/Entity Type

Real Estate

Font styles to use
Serif
Sans Serif

Colors
0054AA
0677BA
7BADD7
CADEEF
E8F1F8
0094D4
00A9DD
6FCCEA
C7EBF8
E9F6FB

Requirements
Must have
• For Sale & our phone number

```html
<!DOCTYPE html>
<html lang="en">
<head>
<meta charset="utf-8">
<title>Granite Hollow Homes – For Sale Sign</title>
<link rel="stylesheet" href="https://fonts.googleapis.com/css2?family=Roboto:wght@400;700&family=Roboto+Slab:wght@900&display=swap">
<style>
  :root {
    --royal: #0650a6;
    --sky: #1a80c4;
    --navy: #141f4d;
    --white: #ffffff;
  }
  * { margin: 0; padding: 0; box-sizing: border-box; }
  html, body { width: 1200px; height: 2998px; overflow: hidden; background: var(--white); }
  .canvas { position: relative; width: 1200px; height: 2998px; }
  .backdrop-blue { position: absolute; left: 0; top: 1385px; width: 1200px; height: 1613px; background: var(--royal); }

  .sign {
    position: absolute; width: 916px; height: 1217px;
    background: var(--white);
    box-shadow: 5px 6px 8px rgba(0,0,0,0.35);
    transform-origin: 0 0;
  }
  .sign--light { left: 142px; top: 83px; }
  .sign--blue { left: 121px; top: 1555px; transform: scale(1.047); }

  .brand-mark { position: absolute; left: 398px; top: 70px; width: 120px; height: 120px; border-radius: 50%; background: var(--royal); }
  .brand-name {
    position: absolute; left: 0; width: 100%; top: 205px; text-align: center;
    font-family: "Roboto", sans-serif; font-weight: 400; font-size: 66px; line-height: 1;
    color: var(--sky); letter-spacing: 1px;
  }
  .roof { position: absolute; left: 0; top: 330px; width: 916px; height: 160px; }

  .headline {
    position: absolute; left: 0; width: 100%; text-align: center;
    font-family: "Roboto Slab", serif; font-weight: 900; font-size: 190px; line-height: 1;
    color: var(--royal);
  }
  .headline--for { top: 470px; }
  .headline--sale { top: 653px; font-size: 196px; }

  .pointer { position: absolute; left: 348px; top: 849px; width: 220px; height: 108px; }

  .contact-label {
    position: absolute; left: 0; width: 100%; top: 979px; text-align: center;
    font-family: "Roboto", sans-serif; font-weight: 400; font-size: 46px; line-height: 1;
    color: var(--sky); letter-spacing: -0.5px;
  }
  .contact-phone {
    position: absolute; left: 0; width: 100%; top: 1022px; text-align: center;
    font-family: "Roboto", sans-serif; font-weight: 700; font-size: 122px; line-height: 1;
    color: var(--navy); letter-spacing: -1px;
  }
  .base-band { position: absolute; left: 0; bottom: 0; width: 100%; height: 53px; background: var(--navy); }
</style>
</head>
<body>
<div class="canvas">
  <div class="backdrop-blue"></div>

  <div class="sign sign--light">
    <div class="brand-mark"></div>
    <div class="brand-name">Granite Hollow Homes</div>
    <svg class="roof" viewBox="0 0 916 160">
      <path d="M30 110 Q330 95 453 19 Q580 95 886 110" fill="none" stroke="var(--navy)" stroke-width="7"/>
      <path d="M30 144 Q330 128 453 52 Q580 128 886 144" fill="none" stroke="var(--sky)" stroke-width="6"/>
    </svg>
    <div class="headline headline--for">FOR</div>
    <div class="headline headline--sale">SALE</div>
    <svg class="pointer" viewBox="0 0 220 108"><polygon points="0,0 220,0 110,108" fill="var(--sky)"/></svg>
    <div class="contact-label">CALL OR TEXT ME AT:</div>
    <div class="contact-phone">(555) 617 3489</div>
    <div class="base-band"></div>
  </div>

  <div class="sign sign--blue">
    <div class="brand-mark"></div>
    <div class="brand-name">Granite Hollow Homes</div>
    <svg class="roof" viewBox="0 0 916 160">
      <path d="M30 110 Q330 95 453 19 Q580 95 886 110" fill="none" stroke="var(--navy)" stroke-width="7"/>
      <path d="M30 144 Q330 128 453 52 Q580 128 886 144" fill="none" stroke="var(--sky)" stroke-width="6"/>
    </svg>
    <div class="headline headline--for">FOR</div>
    <div class="headline headline--sale">SALE</div>
    <svg class="pointer" viewBox="0 0 220 108"><polygon points="0,0 220,0 110,108" fill="var(--sky)"/></svg>
    <div class="contact-label">CALL OR TEXT ME AT:</div>
    <div class="contact-phone">(555) 617 3489</div>
    <div class="base-band"></div>
  </div>
</div>
</body>
</html>
```